Product Label Design

Need a product design for our Epsom salt product, needs to have a luxurious simple feel to it. The picture attached is our brand and wordage on it, the bag we think should be a stand up bag that should be offwhite/creme color. The other picture are products that we like. We updated the packaging to be a Kraft tube box, please see the attached photo for dimensions.

```html
<!DOCTYPE html>
<html lang="en">
<head>
<meta charset="utf-8">
<title>Ascend Epsom Salt – Label Options</title>
<link href="https://fonts.googleapis.com/css2?family=Jost:wght@300;400;500&display=swap" rel="stylesheet">
<style>
  :root {
    --page: #f5f2f2;
    --kraft: #c9a57a;
    --kraft-dark: #b8925f;
    --label: #f1ece5;
    --ink: #5d5d5d;
    --ink-soft: #777;
    --heading: #9d9d9d;
    --sage: #a7bcb1;
    --rule: #8a8a8a;
    --print: #2e2a26;
  }
  * { margin: 0; padding: 0; box-sizing: border-box; }
  html, body { width: 1200px; height: 808px; overflow: hidden; }
  body {
    background: var(--page);
    font-family: "Jost", sans-serif;
    position: relative;
  }
  .option-title {
    position: absolute; top: 140px; width: 354px;
    text-align: center; font-size: 21px; font-weight: 400;
    letter-spacing: 2px; color: var(--heading);
  }
  .pouch {
    position: absolute; top: 185px; width: 354px; height: 500px;
    background: var(--kraft);
  }
  .pouch .tear-line {
    position: absolute; left: 12px; right: 8px; top: 32px;
    border-top: 1px dashed var(--print);
  }
  .pouch .tear-note {
    position: absolute; font-size: 8px; line-height: 1;
    letter-spacing: 0.6px; color: var(--print);
  }
  .pouch .tear-note.cut { left: 73px; top: 21px; }
  .pouch .tear-note.seal { left: 47px; top: 40px; }
  .pouch .zipper {
    position: absolute; left: 0; right: 0; top: 60px; height: 6px;
    border-top: 1px solid var(--kraft-dark); border-bottom: 1px solid var(--kraft-dark);
  }
  .label {
    position: absolute; left: 52px; top: 105px; width: 248px; height: 358px;
    background: var(--label); border-radius: 5px; color: var(--ink);
  }
  .label > * { position: absolute; left: 0; right: 0; text-align: center; line-height: 1.2; }
  .brand { color: var(--ink); font-weight: 500; letter-spacing: 1.5px; }
  .variant { color: var(--sage); font-weight: 500; letter-spacing: 3px; }
  .desc { font-weight: 300; color: var(--ink-soft); }
  .rule { left: 22px; right: 22px; border-top: 1px solid var(--rule); height: 0; }

  .option-a { left: 206px; }
  .option-b { left: 641px; }
</style>
</head>
<body>
  <h2 class="option-title option-a">OPTION A</h2>
  <h2 class="option-title option-b">OPTION B</h2>

  <section class="pouch option-a">
    <span class="tear-note cut">CUT ALONG DOTTED LINE</span>
    <div class="tear-line"></div>
    <span class="tear-note seal">RESEALABLE</span>
    <div class="zipper"></div>
    <div class="label">
      <div class="brand" style="top:28px;font-size:22px;">MAREN</div>
      <div class="variant" style="top:103px;font-size:20px;">ASCEND</div>
      <div class="desc" style="top:162px;font-size:13px;">Pure Epsom Salt</div>
      <div class="desc" style="top:184px;font-size:10px;">(Magnesium Sulfate)</div>
      <div class="desc" style="top:216px;font-size:12px;">Infused with</div>
      <div class="desc" style="top:239px;font-size:12px;">+ Abies sibirica</div>
      <div class="desc" style="top:262px;font-size:12px;">+ Fir Balsam</div>
      <div class="desc" style="top:322px;font-size:11px;">NET WT. 3 LBS (1360 g)</div>
    </div>
  </section>

  <section class="pouch option-b">
    <span class="tear-note cut">CUT ALONG DOTTED LINE</span>
    <div class="tear-line"></div>
    <span class="tear-note seal">RESEALABLE</span>
    <div class="zipper"></div>
    <div class="label">
      <div class="brand" style="top:28px;font-size:34px;">MAREN</div>
      <div class="rule" style="top:92px;"></div>
      <div class="variant" style="top:109px;font-size:16px;">ASCEND</div>
      <div class="desc" style="top:143px;font-size:12px;">US Sourced Pure Epsom Salt</div>
      <div class="desc" style="top:162px;font-size:12px;">(Magnesium Sulfate)</div>
      <div class="desc" style="top:198px;font-size:12px;">+ Abies sibirica</div>
      <div class="desc" style="top:221px;font-size:12px;">+ Fir Balsam</div>
      <div class="desc" style="top:322px;font-size:11px;">NET WT. 3 LBS (1360 g)</div>
    </div>
  </section>
</body>
</html>
```